Banner ads for VL that work with same theme as below banners

Love the banner ads below. Need more with attached photos. But use the same wording, font as in below banner ads. Should be VL size 1200/627 so I can use for Trovique and VL. Looking for great ads to use as VL ads. We do lots of ads so it will be worth your time to enter this contest you will be rewarded with a ton of work. Need several banner ads that work together. So maybe 1 of the dresses, 1 of the sweater, 1 of the leggings, 1 of the jacket

Target Market(s)

Women 24-45

Industry/Entity Type

Fashion

Requirements
Must have
• Banner ads that work for VL and Trovique
Nice to have
• Several options to choose from
Should not have
• not sure

```html
<!DOCTYPE html>
<html lang="en">
<head>
<meta charset="utf-8">
<title>Our Best Sweater Ever – Banner</title>
<link rel="stylesheet" href="https://fonts.googleapis.com/css2?family=Great+Vibes&family=Libre+Baskerville:wght@400;700&family=Open+Sans:wght@400;700&display=swap">
<style>
  :root {
    --bg-light: #f4f4f4;
    --bg-mid: #d9d9d9;
    --bg-dark: #b9b9b9;
    --band-light: rgba(255,255,255,0.55);
    --band-edge: rgba(160,160,160,0.45);
    --ink: #111111;
    --script: #ffffff;
    --script-shadow: rgba(0,0,0,0.55);
    --button-top: #fdfdfd;
    --button-mid: #cfcfcf;
    --button-bottom: #8e8e8e;
    --button-text: #3a3a3a;
    --photo-top: #cfcfcf;
    --photo-bottom: #9a9a9a;
  }
  * { margin: 0; padding: 0; box-sizing: border-box; }
  html, body { width: 1200px; height: 627px; overflow: hidden; }
  body { background: var(--bg-mid); }

  .banner {
    position: relative;
    width: 1200px;
    height: 627px;
    overflow: hidden;
    background:
      radial-gradient(ellipse 520px 230px at 620px 110px, rgba(255,255,255,0.85), rgba(255,255,255,0) 70%),
      radial-gradient(ellipse 700px 420px at 600px 420px, var(--bg-light), rgba(255,255,255,0) 75%),
      linear-gradient(180deg, var(--bg-dark) 0%, var(--bg-mid) 35%, var(--bg-light) 70%, var(--bg-mid) 100%);
  }

  .light-band {
    position: absolute;
    left: 0; right: 0;
    top: 255px;
    height: 60px;
    background: linear-gradient(180deg, var(--band-light), rgba(255,255,255,0.25));
    border-top: 1px solid var(--band-edge);
    border-bottom: 1px solid var(--band-edge);
  }

  .model-photo {
    position: absolute;
    left: 55px;
    top: 28px;
    width: 265px;
    height: 599px;
    border-radius: 110px 110px 0 0;
    background: linear-gradient(180deg, var(--photo-top), var(--photo-bottom));
  }

  .headline {
    position: absolute;
    left: 800px;
    top: 170px;
    width: 330px;
    text-align: center;
  }
  .headline__script {
    display: block;
    font-family: "Great Vibes", cursive;
    color: var(--script);
    font-size: 66px;
    line-height: 1;
    text-shadow: 1px 2px 3px var(--script-shadow);
  }
  .headline__script--top { margin-left: 20px; }
  .headline__script--bottom { margin-top: 4px; margin-left: -40px; }
  .headline__main {
    display: block;
    font-family: "Libre Baskerville", serif;
    font-weight: 700;
    color: var(--ink);
    font-size: 50px;
    letter-spacing: 1px;
    line-height: 1;
    margin-top: 14px;
  }

  .cta-button {
    position: absolute;
    left: 812px;
    top: 458px;
    width: 304px;
    height: 46px;
    border-radius: 23px;
    background: linear-gradient(180deg, var(--button-top) 0%, var(--button-mid) 55%, var(--button-bottom) 100%);
    box-shadow: 0 2px 4px rgba(0,0,0,0.35), inset 0 1px 0 #fff;
    display: flex;
    align-items: center;
    justify-content: center;
    font-family: "Open Sans", sans-serif;
    font-size: 25px;
    color: var(--button-text);
    text-decoration: none;
    letter-spacing: 0.5px;
  }
  .cta-button strong { font-weight: 700; }
  .cta-button span { font-weight: 400; margin: 0 8px; }
</style>
</head>
<body>
  <main class="banner">
    <div class="light-band"></div>
    <div class="model-photo" role="img" aria-label="Photo of a woman with long wavy hair wearing an oversized grey turtleneck knit sweater and black leggings"></div>
    <h1 class="headline">
      <span class="headline__script headline__script--top">Our Best</span>
      <span class="headline__main">SWEATER</span>
      <span class="headline__script headline__script--bottom">Ever</span>
    </h1>
    <a class="cta-button" href="#"><strong>SHOP</strong><span>THE</span><strong>LOOK</strong></a>
  </main>
</body>
</html>
```